Norvale Email Signature Banners – Fabrication Capability Series

www.Norvale.com.au is an Australian engineering and fabrication company specialising in fabrication and welding of :
steel piping spools,
skids and frames,
small volume process steel tanks
and general steel fabrication
We require four distinct banner designs for use in Teldrin Quillmark email signatures. Each banner will highlight a specific capability while maintaining a consistent brand identity.
Deliverables
Four banners total:
Piping Spools Fabrication – focus on precision welding and stainless steel pipework
Skid & Frames Fabrication – highlight skid systems and structural frames
Small Steel Tanks Fabrication – show fabricated tanks and workshop craftsmanship
General Fabrication Solutions – broad steel fabrication theme for company-wide use
Dimensions: 600–700 px wide × 100 px high
Format: PNG (preferred), small file size prefered
Resolution: 72 dpi
Background: non-transparent, industrial or workshop setting
Text examples:
1. Piping Spools Fabrication
Option A: “Expert Fabrication Solutions for Process Piping”
Option B: “Precision Welding for Complex Systems”
Option C: “Delivering Quality in Every Spool”
Option D: “Engineered for Flow, Built for Strength”
2. Skid & Frames Fabrication
Option A: “Custom Engineered Modular Systems”
Option B: “Built Strong. Designed Smart.”
Option C: “Reliable Frames for Industrial Performance”
Option D: “Modular Fabrication for Seamless Integration”
3. Small Steel Tanks Fabrication
Option A: “Precision Built for Your Needs”
Option B: “Compact Strength. Proven Durability.”
Option C: “Fabricated for Performance and Longevity”
Option D: “Small Tanks. Big Reliability.”
4. General Fabrication Solutions
Option A: “Quality Craftsmanship, Proven Results”
Option B: “Your Partner in Precision Fabrication”
Option C: “Engineering Excellence in Every Weld”
Option D: “Australian Fabrication. Global Standards.”
Style Direction
Clean, professional, and engineering‑focused
Use Norvale brand colours
Blend photo realism with vector clarity (no heavy gradients)
Include subtle industrial textures or workshop imagery
Typography: bold sans‑serif, legible at small scale
Usage Context
These banners will appear at the bottom of staff email signatures via Quillmark Email Signature Tool for Teldrin 365, so clarity and fast loading are essential. No Logo is required in the banners.
Reference
Existing Norvale signature is attached. Colour palette to match the signature style and logo.
Target Market(s)
Engineering and construction companies,
Industry/Entity Type
Engineering fabrication design

```html
<!DOCTYPE html>
<html lang="en">
<head>
<meta charset="UTF-8">
<title>Norvale – Piping Spools Fabrication Banner</title>
<link rel="stylesheet" href="https://fonts.googleapis.com/css2?family=Poppins:wght@400;700&display=swap">
<style>
  :root {
    --brand-blue: #0b5ab4;
    --brand-blue-deep: #0a55ab;
    --steel-light: #d3dbe2;
    --steel-mid: #a9b8c6;
    --steel-shadow: #7f93a6;
    --accent-blue: #1f66d1;
    --text-white: #ffffff;
  }
  * { margin: 0; padding: 0; box-sizing: border-box; }
  html, body {
    width: 1200px;
    height: 200px;
    overflow: hidden;
    background: var(--brand-blue);
  }
  .banner {
    position: relative;
    width: 1200px;
    height: 200px;
    overflow: hidden;
    background: linear-gradient(90deg, var(--brand-blue-deep) 0%, var(--brand-blue) 60%);
    font-family: "Poppins", sans-serif;
    color: var(--text-white);
  }
  .banner__photo {
    position: absolute;
    top: 0;
    right: 0;
    width: 460px;
    height: 200px;
    background:
      linear-gradient(90deg, var(--brand-blue) 0%, rgba(11, 90, 180, 0.6) 18%, rgba(11, 90, 180, 0) 38%),
      linear-gradient(180deg, var(--steel-light) 0%, var(--steel-mid) 55%, var(--accent-blue) 70%, var(--steel-shadow) 85%, var(--steel-light) 100%);
  }
  .banner__copy {
    position: absolute;
    left: 41px;
    top: 48px;
  }
  .banner__title {
    font-weight: 700;
    font-size: 43px;
    line-height: 1.1;
    letter-spacing: -0.2px;
  }
  .banner__tagline {
    margin-top: 10px;
    font-weight: 400;
    font-size: 32px;
    line-height: 1.1;
  }
</style>
</head>
<body>
  <div class="banner">
    <div class="banner__photo" role="img" aria-label="Industrial plant room with grey process pipework, blue valve and blue pump motor above a water tank"></div>
    <div class="banner__copy">
      <h1 class="banner__title">Piping Spools Fabrication</h1>
      <p class="banner__tagline">“Engineered for Flow, Built for Strength”</p>
    </div>
  </div>
</body>
</html>
```